KerrLow Farm

Need a nice simple clean double sided business card that has our logo and info on:
Kerr Low Farm
Martin & Felicity Kerr Low
kerrlowfarm@mailbarn.example
Martin: 1-780-555-0148
Felicity: 1-780-555-0193
Instagram @ kerrlow_farm

Contact Information for Business Card

Martin & Felicity Kerr Low kerrlowfarm@mailbarn.example Martin: 1-780-555-0148 Felicity: 1-780-555-0193

```html
<!DOCTYPE html>
<html lang="en">
<head>
<meta charset="utf-8">
<title>Kerr Low Farm – Business Card</title>
<link href="https://fonts.googleapis.com/css2?family=Montserrat:wght@500;700&display=swap" rel="stylesheet">
<style>
  :root{
    --farm-green:#6aa343;
    --harvest-orange:#f7991f;
    --ink:#1b1b1b;
    --paper:#ffffff;
    --backdrop:#b4b4b4;
  }
  *{box-sizing:border-box;margin:0;padding:0}
  html,body{width:1200px;height:1200px;overflow:hidden}
  body{background:var(--backdrop);font-family:"Montserrat",sans-serif;position:relative}
  .card{position:absolute;left:228px;width:746px;height:428px;overflow:hidden}
  .card--front{top:114px;background:var(--paper)}
  .card--back{top:583px;background:var(--farm-green)}
  .header-band{position:absolute;left:0;top:0;width:100%;height:96px;background:var(--farm-green)}
  .header-stripe{position:absolute;left:0;top:104px;width:100%;height:8px;background:var(--harvest-orange)}
  .farm-title{position:absolute;left:38px;top:206px;font-size:25px;font-weight:700;color:var(--farm-green);letter-spacing:.2px}
  .owners{position:absolute;left:40px;top:255px;font-size:19px;font-weight:700;color:var(--farm-green)}
  .owners .owners__second{color:var(--harvest-orange)}
  .title-rule{position:absolute;left:40px;top:285px;width:31px;height:4px;background:var(--farm-green)}
  .contacts{position:absolute;left:40px;top:296px;list-style:none}
  .contacts li{display:flex;align-items:center;height:30px;font-size:19px;font-weight:500;color:var(--ink)}
  .contacts svg{width:19px;height:19px;margin-right:12px;flex:none}
  .brand{position:absolute;display:flex;flex-direction:column;align-items:center}
  .brand__circle{border-radius:50%}
  .brand__name{font-weight:700;letter-spacing:1px;white-space:nowrap}
  .card--front .brand{left:420px;top:182px;width:300px}
  .card--front .brand__circle{width:110px;height:110px;border:3px solid var(--farm-green)}
  .card--front .brand__name{margin-top:16px;font-size:26px;color:var(--farm-green)}
  .card--back .brand{left:173px;top:105px;width:400px}
  .card--back .brand__circle{width:148px;height:148px;border:4px solid var(--paper)}
  .card--back .brand__name{margin-top:26px;font-size:34px;color:var(--paper)}
</style>
</head>
<body>
  <section class="card card--front">
    <div class="header-band"></div>
    <div class="header-stripe"></div>

    <h1 class="farm-title">KERR LOW FARM</h1>
    <p class="owners">MARTIN &amp; <span class="owners__second">FELICITY KERR LOW</span></p>
    <div class="title-rule"></div>

    <ul class="contacts">
      <li>
        <svg viewBox="0 0 24 24" aria-hidden="true"><path fill="var(--farm-green)" d="M6.6 10.8a15 15 0 0 0 6.6 6.6l2.2-2.2c.3-.3.7-.4 1-.2 1.1.4 2.3.6 3.6.6.6 0 1 .4 1 1V20c0 .6-.4 1-1 1A17 17 0 0 1 3 4c0-.6.4-1 1-1h3.5c.6 0 1 .4 1 1 0 1.3.2 2.5.6 3.6.1.3 0 .7-.2 1z"/></svg>
        kerrlowfarm@mailbarn.example
      </li>
      <li>
        <svg viewBox="0 0 24 24" aria-hidden="true"><path fill="var(--farm-green)" d="M2 5h20v14H2z"/><path fill="none" stroke="#fff" stroke-width="1.6" d="M2 5l10 8 10-8M2 19l7-7M22 19l-7-7"/></svg>
        Martin: 1-780-555-0148
      </li>
      <li>
        <svg viewBox="0 0 24 24" aria-hidden="true"><circle cx="12" cy="12" r="10" fill="var(--farm-green)"/><path fill="#fff" d="M7 6c2 1 3 3 2 5-1 1-3 1-3 3 0 1 1 2 1 3-2-1-4-4-3-7 1-2 2-3 3-4zm8 2c2 0 3 2 2 4s-3 1-3 3 2 2 1 4c2-1 4-3 4-6 0-2-2-5-4-5z"/></svg>
        Felicity: 1-780-555-0193
      </li>
    </ul>

    <div class="brand">
      <div class="brand__circle"></div>
      <p class="brand__name">KERR LOW FARM</p>
    </div>
  </section>

  <section class="card card--back">
    <div class="brand">
      <div class="brand__circle"></div>
      <p class="brand__name">KERR LOW FARM</p>
    </div>
  </section>
</body>
</html>
```